Letterhead Design for Law Firm that Specializes in Property Damage Litigation

We are looking for a redesign of our letterhead. Our current letterhead lists all of our current staff members and we'd like to come up with a design that does NOT list all of the staff members so that it does not need to be updated with every newly hired employee. Must be in editable format.

We are a law firm that specializes in property damage, so we need something that is professional, yet modern. The final design should use our existing logo and should use a blue color scheme (alternate colors would be gray, black, and white).

Industry/Entity Type

Legal

Colors
0054AA
0677BA
7BADD7
CADEEF
E8F1F8

```html
<!DOCTYPE html>
<html lang="en">
<head>
<meta charset="utf-8">
<title>Hartwell Sloane &amp; Pryce Letterhead</title>
<link href="https://fonts.googleapis.com/css2?family=Figtree:wght@400;500;600&display=swap" rel="stylesheet">
<style>
  :root {
    --backdrop: #e0e0e0;
    --paper: #ffffff;
    --navy: #0b3163;
    --ink: #2b2b2b;
    --ink-soft: #444444;
    --grey: #666666;
    --rule: #cfcfcf;
    --sig-tone: #ececec;
  }
  * { margin: 0; padding: 0; box-sizing: border-box; }
  html, body { width: 1200px; height: 1200px; overflow: hidden; }
  body { background: var(--backdrop); font-family: "Figtree", Arial, sans-serif; position: relative; }
  .letterhead { position: absolute; left: 216px; top: 76px; width: 768px; height: 1047px; background: var(--paper); }

  .brand { position: absolute; top: 44px; left: 0; width: 100%; text-align: center; }
  .brand-name { display: inline-flex; align-items: center; gap: 10px; color: var(--navy); font-weight: 600; font-size: 25px; letter-spacing: 0.5px; }
  .brand-mark { width: 14px; height: 14px; background: var(--navy); }
  .brand-tagline { margin-top: 16px; font-size: 10px; font-weight: 600; letter-spacing: 2.6px; color: var(--grey); }

  .salutation { position: absolute; left: 53px; top: 259px; font-size: 22px; font-weight: 600; color: var(--ink-soft); }
  .letter-body { position: absolute; left: 55px; top: 303px; width: 659px; font-size: 17.4px; line-height: 21.3px; color: var(--ink); text-align: justify; }
  .letter-body p + p { margin-top: 21.3px; }

  .sign-off { position: absolute; left: 55px; top: 758px; width: 180px; height: 105px; }
  .signature-area { position: absolute; left: 0; top: 0; width: 170px; height: 105px; background: var(--sig-tone); border-radius: 4px; }
  .signer-name { position: absolute; left: 8px; top: 4px; font-size: 11px; color: var(--grey); }
  .signer-role { position: absolute; left: 8px; top: 20px; font-size: 8px; color: var(--grey); }

  .website { position: absolute; top: 910px; left: 0; width: 100%; text-align: center; font-size: 17px; color: var(--navy); }

  .office { position: absolute; top: 950px; color: var(--ink); font-size: 10px; }
  .office-phil { left: 66px; }
  .office-nj { left: 414px; top: 946px; }
  .office-title { font-size: 14px; font-weight: 600; color: var(--navy); margin-bottom: 6px; }
  .office-line { display: flex; align-items: center; gap: 5px; height: 16px; }
  .office-line svg { width: 11px; height: 11px; fill: var(--navy); flex: none; }
  .office-line .gap { width: 10px; }
  .office-divider { position: absolute; left: 380px; top: 952px; width: 1px; height: 59px; background: var(--rule); }

  .footer-band { position: absolute; left: 0; bottom: 0; width: 768px; height: 22px; }
</style>
</head>
<body>
  <div class="letterhead">
    <header class="brand">
      <div class="brand-name"><span class="brand-mark"></span>Hartwell Sloane &amp; Pryce</div>
      <div class="brand-tagline">THE PROPERTY DAMAGE ATTORNEYS</div>
    </header>

    <h1 class="salutation">Dear Mr. John,</h1>

    <div class="letter-body">
      <p>Lorem ipsum dolor sit amet, consectetuer adipiscing elit, sed diam nonummy nibh euismod tincidunt ut laoreet dolore magna aliquam erat volutpat. Ut wisi enim ad minim veniam, quis nostrud exerci tation ullamcorper suscipit lobortis nisl ut aliquip ex ea commodo consequat. Duis autem vel eum iriure dolor in hendrerit in vulputate velit esse molestie consequat, vel illum dolore eu feugiat nulla facilisis at vero eros et accumsan et iusto odio dignissim qui blandit praesent luptatum zzril delenit augue duis dolore te feugait nulla facilisi.</p>
      <p>Lorem ipsum dolor sit amet, cons ectetuer adipiscing elit, sed diam nonummy nibh euismod tincidunt ut laoreet dolore magna aliquam erat volutpat. Ut wisi Lorem ipsum dolor sit amet, consectetuer adipiscing elit, sed diam nonummy nibh euismod tincidunt ut laoreet dolore magna aliquam erat volutpat. Ut wisi enim ad minim veniam, quis nostrud exerci tation ullamcorper suscipit lobortis nisl ut aliquip ex ea commodo consequat. Duis autem vel eum iriure dolor in hendrerit in vulputate velit esse molestie consequat,Lorem ipsum dolor sit amet, cons ectetuer adipiscing elit, sed diam nonummy nibh euismod tincidunt ut laoreet dolore magna aliquam erat volutpat.</p>
    </div>

    <div class="sign-off">
      <div class="signature-area" role="img" aria-label="Handwritten signature of the office manager"></div>
      <div class="signer-name">John Doe</div>
      <div class="signer-role">Office Manager</div>
    </div>

    <div class="website">www.hsplawgroup.com</div>

    <section class="office office-phil">
      <div class="office-title">Philadelphia Office</div>
      <div class="office-line">
        <svg viewBox="0 0 24 24"><path d="M6.6 10.8a15 15 0 0 0 6.6 6.6l2.2-2.2c.3-.3.7-.4 1-.2 1.1.4 2.3.6 3.6.6.6 0 1 .4 1 1V20c0 .6-.4 1-1 1A17 17 0 0 1 3 4c0-.6.4-1 1-1h3.5c.6 0 1 .4 1 1 0 1.3.2 2.5.6 3.6.1.3 0 .7-.2 1z"/></svg>
        <span>(215) 555-0142</span><span class="gap"></span>
        <svg viewBox="0 0 24 24"><path d="M6 2h9v5H6zM3 8h18v13H3zm3 3v2h2v-2zm4 0v2h2v-2zm4 0v2h2v-2zm-8 4v2h2v-2zm4 0v2h2v-2zm4 0v2h2v-2z"/></svg>
        <span>(215) 555-0187</span>
      </div>
      <div class="office-line">
        <svg viewBox="0 0 24 24"><path d="M12 2a7 7 0 0 0-7 7c0 5 7 13 7 13s7-8 7-13a7 7 0 0 0-7-7zm0 9.5A2.5 2.5 0 1 1 12 6.5a2.5 2.5 0 0 1 0 5z"/></svg>
        <span>820 Market Square Blvd. Suite 410 Philadelphia, PA 19107</span>
      </div>
    </section>

    <div class="office-divider"></div>

    <section class="office office-nj">
      <div class="office-title">New Jersey Office</div>
      <div class="office-line" style="margin-top:4px">
        <svg viewBox="0 0 24 24"><path d="M6.6 10.8a15 15 0 0 0 6.6 6.6l2.2-2.2c.3-.3.7-.4 1-.2 1.1.4 2.3.6 3.6.6.6 0 1 .4 1 1V20c0 .6-.4 1-1 1A17 17 0 0 1 3 4c0-.6.4-1 1-1h3.5c.6 0 1 .4 1 1 0 1.3.2 2.5.6 3.6.1.3 0 .7-.2 1z"/></svg>
        <span>(856) 555-0163</span><span class="gap"></span>
        <svg viewBox="0 0 24 24"><path d="M6 2h9v5H6zM3 8h18v13H3zm3 3v2h2v-2zm4 0v2h2v-2zm4 0v2h2v-2zm-8 4v2h2v-2zm4 0v2h2v-2zm4 0v2h2v-2z"/></svg>
        <span>(856) 555-0119</span>
      </div>
      <div class="office-line">
        <svg viewBox="0 0 24 24"><path d="M12 2a7 7 0 0 0-7 7c0 5 7 13 7 13s7-8 7-13a7 7 0 0 0-7-7zm0 9.5A2.5 2.5 0 1 1 12 6.5a2.5 2.5 0 0 1 0 5z"/></svg>
        <span>275 Haddon Ridge Road, Suite 300 Cherry Hill, NJ 08002</span>
      </div>
    </section>

    <svg class="footer-band" viewBox="0 0 768 22" preserveAspectRatio="none">
      <polygon points="0,0 389,0 379,22 0,22" fill="var(--navy)"/>
      <polygon points="399,0 768,0 768,22 389,22" fill="var(--grey)"/>
    </svg>
  </div>
</body>
</html>
```